Buch-/eBook-Cover Budgetplanung
Zielgruppe
Ich bin Autorin und verkaufe unter meiner Marke SpargutFee Bücher und handgemachte Produkte rund um Budgetplanung und bewussten Umgang mit Geld. Meine Zielgruppe sind Frauen ab 45, die ihre Finanzen ordnen und bewusster leben möchten. Sie mögen eine ruhige, hochwertige, leicht nostalgische Ästhetik und werden von lauten, grellen Designs abgeschreckt.
Aufgabenstellung
Buchcover 'Ohne Kassenbon' (PLV), Auftakt einer Cover-Serie
Das Buch:
Ratgeber über bewussten Konsumverzicht: ein Jahr Kaufpause mit monatlichen Challenges. Warm und ermutigend, kein Verbotsbuch. Zielgruppe: Frauen ab 45, die eine ruhige, hochwertige, leicht nostalgische Ästhetik mögen.
Texte auf dem Cover:
Titel: Ohne Kassenbon
Untertitel: Die Null-Kauf-Aufgabe: Ein Jahr bewusst nicht kaufen, Geld sparen und herausfinden, was du wirklich brauchst
Autorin: Helga Brunnmeier
Serie:
Weitere Geld-Ratgeber von mir erhalten danach Cover im selben Stil. Gesucht ist also ein wiederholbares Layout, bei dem sich pro Buch nur Titel und Motiv ändern. Der Gewinner erhält die Folgecover als Direktaufträge.
Stil (Referenzbilder anbei, bitte verbindlich umsetzen):
Marke SpargutFee: Graublau (#95a9af) und Creme, Gold nur als Akzent. Vertikale Streifen als Markenmuster, weiße Spitzenborte, schwarze handgezeichnete Schleife (PNG liegt bei). Schriften: Cormorant Garamond für Versalien, Sloop Pro, Kalligrafieschrift für Akzente. Wirkung: elegantes, feminines Vintage. Das Buchinnere ist bereits in diesem Stil gestaltet (Beispielseiten anbei), das Cover soll dazu passen.
Bitte nicht: Geldscheine, Münzen, Sparschweine, Einkaufstüten, rote Verbotssymbole, grelle Farben, Rosa, überfüllte Layouts.
Wichtigstes Kriterium:
Der Titel muss als kleines Wendor-Vorschaubild klar lesbar sein.
Lieferumfang:
E-Book-Cover (JPG, 2560 x 1600 px), PLV-Print-Umschlag (6 x 9 Zoll, 159 Seiten, Farbdruck)
Das Design darf nicht zu überladen sein.

```html
<!DOCTYPE html>
<html lang="de">
<head>
<meta charset="utf-8">
<title>Ohne Kassenbon – Umschlag</title>
<link href="https://fonts.googleapis.com/css2?family=Cormorant+Garamond:wght@500;600;700&family=EB+Garamond:ital,wght@0,400;0,500;1,400&family=Great+Vibes&display=swap" rel="stylesheet">
<style>
  :root {
    --blue-grey: #95a9af;
    --cream: #f8f4ee;
    --cream-soft: #fbf8f3;
    --gold: #c9a464;
    --gold-deep: #b8894a;
    --ink: #1f1d1b;
    --lace: #d9dfe0;
    --guide-blue: #3a4cff;
    --guide-dark: #3c4347;
    --trim: #2d2f31;
  }
  * { margin: 0; padding: 0; box-sizing: border-box; }
  html, body { width: 1200px; height: 886px; overflow: hidden; background: var(--blue-grey); }
  .canvas { position: relative; width: 1200px; height: 886px; background: var(--blue-grey); overflow: hidden; }

  .cover-sheet {
    position: absolute; left: 50px; top: 50px; width: 1100px; height: 786px;
    border: 1px solid var(--trim);
    background: var(--blue-grey);
  }
  .stripes {
    position: absolute; top: 0; bottom: 0;
    background: repeating-linear-gradient(90deg,
      var(--blue-grey) 0 53px, var(--cream) 53px 88px);
  }
  .stripes--back { left: 0; width: 494px; }
  .stripes--front { left: 612px; width: 488px; background-position: 8px 0; }

  .lace-border { position: absolute; top: 0; bottom: 0; width: 40px; background: linear-gradient(90deg, var(--lace), #c2ccce); }
  .lace-border--left { left: 0; }
  .lace-border--right { right: 0; width: 46px; }

  .spine { position: absolute; left: 494px; top: 0; width: 112px; height: 786px; background: var(--blue-grey); }
  .guide { position: absolute; top: 0; height: 886px; width: 0; }
  .guide--blue { border-left: 1px dashed var(--guide-blue); }
  .guide--dark { border-left: 1px dashed var(--guide-dark); }

  .spine-bow { position: absolute; left: 50%; top: 70px; width: 22px; height: 18px; margin-left: -11px; background: var(--cream); opacity: .85; border-radius: 3px; }
  .spine-text {
    position: absolute; left: 50%; top: 110px;
    transform: translateX(-50%); writing-mode: vertical-rl;
    font-family: "Cormorant Garamond", serif; font-weight: 500;
    font-size: 22px; color: var(--cream); white-space: nowrap; letter-spacing: .2px;
  }
  .spine-text .spine-star { color: var(--gold); margin: 14px 0; }

  /* back cover */
  .blurb-card { position: absolute; left: 56px; top: 119px; width: 418px; height: 552px; }
  .blurb-card svg.card-shape { position: absolute; inset: 0; }
  .blurb-content { position: absolute; inset: 0; padding: 26px 30px 0 30px; font-family: "EB Garamond", serif; color: var(--ink); }
  .laurel { display: block; margin: 0 auto; width: 70px; height: 22px; background: var(--gold); opacity: .75; border-radius: 11px; }
  .blurb-heading {
    font-family: "Great Vibes", cursive; font-weight: 400; text-align: center;
    font-size: 33px; line-height: 1.05; margin-top: 18px; transform: rotate(-4deg);
  }
  .gold-rule { display: flex; align-items: center; gap: 8px; margin: 18px 6px 14px; color: var(--gold); font-size: 16px; }
  .gold-rule::before, .gold-rule::after { content: ""; flex: 1; height: 1px; background: var(--gold); }
  .blurb-text p { font-size: 13.2px; line-height: 1.42; text-align: justify; margin-bottom: 8px; }
  .dot-rule { display: flex; align-items: center; gap: 6px; margin: 8px 6px 12px; }
  .dot-rule::before, .dot-rule::after { content: ""; flex: 1; height: 1px; background: var(--gold); }
  .dot-rule span { width: 5px; height: 5px; border-radius: 50%; background: var(--gold); }
  .author-bio { font-style: italic; font-size: 13.2px; line-height: 1.42; text-align: justify; }
  .laurel--bottom { margin-top: 18px; }

  /* front cover */
  .title-label { position: absolute; left: 615px; top: 106px; width: 440px; height: 532px; }
  .title-label svg.label-shape { position: absolute; inset: 0; overflow: visible; }
  .label-bow { position: absolute; left: 50%; top: 22px; width: 40px; height: 28px; margin-left: -20px; background: var(--ink); border-radius: 50% 50% 40% 40%; opacity: .85; }
  .book-title {
    position: absolute; left: 0; right: 0; top: 68px; text-align: center;
    font-family: "Cormorant Garamond", serif; font-weight: 700; color: var(--ink);
    font-size: 60px; line-height: .98;
  }
  .book-subtitle {
    position: absolute; left: 0; right: 0; top: 200px; text-align: center;
    font-family: "Cormorant Garamond", serif; font-weight: 500; color: var(--gold);
    font-size: 30px; white-space: nowrap;
  }
  .book-subtitle .script { font-family: "Great Vibes", cursive; font-size: 31px; }
  .cart-motif {
    position: absolute; left: 142px; top: 248px; width: 146px; height: 150px;
    background: radial-gradient(ellipse at 50% 50%, #c98f55 0%, #d9ae7f 55%, rgba(248,244,238,0) 75%);
    border-radius: 10px;
  }
  .sprig-motif { position: absolute; left: 322px; top: 280px; width: 24px; height: 66px; background: #efe6d6; border-radius: 12px; }
  .book-tagline {
    position: absolute; left: 70px; right: 70px; top: 404px; text-align: center;
    font-family: "EB Garamond", serif; font-size: 18px; line-height: 1.12; color: var(--ink);
  }
  .label-laurel { position: absolute; left: 50%; top: 478px; width: 60px; height: 16px; margin-left: -30px; background: var(--gold); opacity: .75; border-radius: 8px; }
  .author-name {
    position: absolute; left: 612px; width: 488px; top: 664px; text-align: center;
    font-family: "Cormorant Garamond", serif; font-weight: 600; color: var(--ink);
    font-size: 34px;
  }
</style>
</head>
<body>
<div class="canvas">
  <div class="cover-sheet">
    <div class="stripes stripes--back"></div>
    <div class="stripes stripes--front"></div>
    <div class="lace-border lace-border--left" role="img" aria-label="Weiße Spitzenborte am linken Rand"></div>
    <div class="lace-border lace-border--right" role="img" aria-label="Weiße Spitzenborte am rechten Rand"></div>

    <div class="spine">
      <div class="spine-bow" role="img" aria-label="Kleine Schleife"></div>
      <div class="spine-text">Ohne Kassenbon Die Null-Kauf-Aufgabe <span class="spine-star">✻</span> Helga Brunnmeier</div>
    </div>

    <section class="blurb-card">
      <svg class="card-shape" viewBox="0 0 418 552" width="418" height="552">
        <path d="M36 0 H382 A36 36 0 0 0 418 36 V516 A36 36 0 0 0 382 552 H36 A36 36 0 0 0 0 516 V36 A36 36 0 0 0 36 0 Z" fill="#fbf8f3"/>
        <path d="M42 10 H376 A32 32 0 0 0 408 42 V510 A32 32 0 0 0 376 542 H42 A32 32 0 0 0 10 510 V42 A32 32 0 0 0 42 10 Z" fill="none" stroke="#c9a464" stroke-width="1" stroke-dasharray="2 3"/>
      </svg>
      <div class="blurb-content">
        <span class="laurel" role="img" aria-label="Goldener Zweig"></span>
        <h2 class="blurb-heading">Was wäre, wenn du ein<br>Jahr lang nichts kaufst?</h2>
        <div class="gold-rule">✻</div>
        <div class="blurb-text">
          <p>Kein neues Oberteil. Keine Deko. Kein „Das gönn ich mir jetzt mal“.</p>
          <p>Klingt nach Verzicht? Ist es nicht. Dieses Buch verbietet dir nichts. Es lädt dich ein, ein Jahr lang bewusst zu leben, statt nebenbei zu konsumieren.</p>
          <p>Es begleitet dich durch dein Jahr: mit Checklisten zu jedem Thema und zwölf Null-Kauf-Aufgaben zum Ankreuzen. Du findest heraus, was du wirklich brauchst, warum du oft nur aus Gewohnheit oder Frust kaufst und was du mit dem gesparten Geld alles erreichen kannst.</p>
          <p>Am Ende wirst du merken: Dir fehlt nichts. Aber du hast mehr. Mehr Geld, mehr Klarheit, mehr Leben.</p>
        </div>
        <div class="dot-rule"><span></span></div>
        <p class="author-bio">Helga Brunnmeier lebt seit den 1990er Jahren nach der Umschlagmethode und hat ihren Weg aus Schulden und Konsumdruck selbst gemeistert. Sie weiß: Verzicht ist kein Verlust. Er ist der Anfang von etwas Besserem.</p>
        <span class="laurel laurel--bottom" role="img" aria-label="Goldener Zweig"></span>
      </div>
    </section>

    <section class="title-label">
      <svg class="label-shape" viewBox="0 0 440 532" width="440" height="532">
        <defs>
          <path id="label-outline" d="M60 40 Q140 44 200 22 Q220 6 240 22 Q300 44 380 40 Q426 38 424 84 Q414 150 428 230 Q440 330 412 400 Q388 450 300 480 Q250 494 236 514 Q220 528 204 514 Q190 494 140 480 Q52 450 28 400 Q0 330 12 230 Q26 150 16 84 Q14 38 60 40 Z"/>
        </defs>
        <use href="#label-outline" fill="#fbf8f3" stroke="#ffffff" stroke-width="8"/>
        <use href="#label-outline" fill="none" stroke="#c9a464" stroke-width="1.2" vector-effect="non-scaling-stroke" transform="translate(220 266) scale(0.955) translate(-220 -266)"/>
        <use href="#label-outline" fill="none" stroke="#c9a464" stroke-width="1" stroke-dasharray="2 3" vector-effect="non-scaling-stroke" transform="translate(220 266) scale(0.91) translate(-220 -266)"/>
      </svg>
      <span class="label-bow" role="img" aria-label="Schwarze handgezeichnete Schleife"></span>
      <h1 class="book-title">Ohne<br>Kassenbon</h1>
      <p class="book-subtitle">Die Null-Kauf-<span class="script">Aufgabe</span></p>
      <div class="cart-motif" role="img" aria-label="Gezeichneter Einkaufswagen in Kupfertönen"></div>
      <div class="sprig-motif" role="img" aria-label="Blasser Zweig"></div>
      <p class="book-tagline">Ein Jahr bewusst nicht kaufen,<br>Geld sparen und herausfinden,<br>was du wirklich brauchst</p>
      <span class="label-laurel" role="img" aria-label="Goldener Zweig"></span>
    </section>

    <p class="author-name">Helga Brunnmeier</p>
  </div>

  <span class="guide guide--blue" style="left:541px"></span>
  <span class="guide guide--blue" style="left:579px"></span>
  <span class="guide guide--dark" style="left:622px"></span>
  <span class="guide guide--dark" style="left:657px"></span>
</div>
</body>
</html>
```